Banner Designs for Drone Defense Ad Campaign

Corvane is a security consulting and services company that offers a service called SkyMindful. SkyMindful helps our customers identify security risks from drones and develops comprehensive protection programs. We are looking for a designer to create a banner ad in three sizes for our campaign.
Target Market(s)
Our campaign is geared to the sports and entertainment industry, specifically large event venues and their security operation.
Industry/Entity Type
Security
Font styles to use
Other font styles liked:
- Raleway
Requirements
Must have
- Banner Objective
The visual and textual content of the banner should prompt the viewer to quickly identify the service offered and the information that is available to download.
Banner Design
Logo: SkyMindful logo
Call to Action Button in Red: Get It Here (On Right or or Upper Right)
Title in Larger Font: Guide to UAS Risk Mitigation
Subtitle in smaller Font: 5 Steps to Develop Your Comprehensive UAS Defense Program
Background: Stadium with a drone flying in foreground
Font: Raleway
Banner Sizes
1 - 1200x670 pixels
2 - 1510x196 pixels
3 - 1200x628 pixels

```html
<!DOCTYPE html>
<html lang="en">
<head>
<meta charset="utf-8">
<title>SkyMindful Banner Set</title>
<link rel="stylesheet" href="https://fonts.googleapis.com/css2?family=Montserrat:wght@700&family=Raleway:wght@300;400;500;700;800&display=swap">
<style>
  :root {
    --sheet: #ffffff;
    --ink: #111111;
    --white: #ffffff;
    --brand-blue: #1876c6;
    --accent-red: #ff4646;
    --cta-top: #ff2a1a;
    --cta-bottom: #e20c0c;
    --panel: rgba(20, 18, 12, 0.62);
    --panel-edge: rgba(255, 255, 255, 0.45);
    --sky: #140c12;
    --glow: #e9a35a;
    --crowd: #5e1c18;
    --field: #4e5c2c;
  }
  * { box-sizing: border-box; margin: 0; padding: 0; }
  html, body {
    width: 1059px; height: 1200px; overflow: hidden;
    background: var(--sheet);
  }
  .sheet { position: relative; width: 1059px; height: 1200px; }

  .size-label {
    position: absolute; left: 21px;
    font-family: "Montserrat", sans-serif; font-weight: 700;
    font-size: 26px; color: var(--ink); letter-spacing: 0.5px;
  }

  .banner {
    position: absolute; overflow: hidden;
    font-family: "Raleway", sans-serif; color: var(--white);
  }
  .banner--670 { left: 173px; top: 56px; width: 847px; height: 473px; }
  .banner--628 { left: 173px; top: 571px; width: 847px; height: 443px; }
  .banner--strip { left: 0; top: 1053px; width: 1059px; height: 138px; }

  .stadium-photo {
    position: absolute; inset: 0;
    background:
      radial-gradient(ellipse 30% 22% at 2% 40%, rgba(233,163,90,0.55), transparent 70%),
      radial-gradient(ellipse 30% 18% at 96% 6%, rgba(240,190,130,0.7), transparent 70%),
      radial-gradient(ellipse 35% 22% at 62% 42%, rgba(235,235,235,0.35), transparent 70%),
      linear-gradient(180deg, var(--sky) 0%, #2a1416 30%, var(--crowd) 55%, #6a2a1e 72%, var(--field) 88%, #3e4a22 100%);
  }
  .banner--strip .stadium-photo {
    background:
      radial-gradient(ellipse 18% 60% at 95% 20%, rgba(240,190,130,0.55), transparent 70%),
      radial-gradient(ellipse 12% 50% at 106px 100%, rgba(220,220,220,0.2), transparent 70%),
      linear-gradient(180deg, #2a1214 0%, var(--crowd) 45%, #6a2a1e 75%, var(--field) 100%);
  }

  .brand-name {
    position: absolute; font-weight: 500; color: var(--white);
    white-space: nowrap; line-height: 1;
  }
  .brand-byline {
    position: absolute; font-weight: 400; color: var(--white);
    white-space: nowrap; line-height: 1; text-align: right;
  }

  .headline-lead {
    position: absolute; font-weight: 300; line-height: 1; white-space: nowrap;
  }
  .headline-bar { position: absolute; background: var(--brand-blue); }
  .headline-key {
    position: absolute; font-weight: 800; line-height: 1; white-space: nowrap;
    letter-spacing: -1.5px;
  }

  .subtitle-panel { position: absolute; }
  .subtitle-panel svg { position: absolute; inset: 0; width: 100%; height: 100%; }
  .subtitle-text {
    position: absolute; font-weight: 400; line-height: 1.3; white-space: nowrap;
  }
  .subtitle-text .step-count { color: var(--accent-red); font-weight: 700; }

  .cta-button {
    position: absolute; display: flex; align-items: center; justify-content: center;
    background: linear-gradient(180deg, var(--cta-top), var(--cta-bottom));
    border-radius: 8px; box-shadow: 0 3px 0 rgba(150, 0, 0, 0.7);
    font-weight: 700; letter-spacing: 2px; color: var(--white);
  }

  /* 1200x670 */
  .banner--670 .brand-name { left: 59px; top: 72px; font-size: 40px; }
  .banner--670 .brand-byline { left: 150px; width: 154px; top: 114px; font-size: 21px; }
  .banner--670 .headline-lead { left: 47px; top: 182px; font-size: 48px; }
  .banner--670 .headline-bar { left: 31px; top: 270px; width: 441px; height: 28px; }
  .banner--670 .headline-key { left: 45px; top: 230px; font-size: 70px; }
  .banner--670 .subtitle-panel { left: 50px; top: 332px; width: 342px; height: 100px; }
  .banner--670 .subtitle-text { left: 81px; top: 350px; font-size: 25px; }
  .banner--670 .cta-button { left: 561px; top: 347px; width: 248px; height: 54px; font-size: 21px; }

  /* 1200x628 */
  .banner--628 .brand-name { left: 75px; top: 70px; font-size: 40px; }
  .banner--628 .brand-byline { left: 166px; width: 154px; top: 112px; font-size: 21px; }
  .banner--628 .headline-lead { left: 64px; top: 180px; font-size: 48px; }
  .banner--628 .headline-bar { left: 47px; top: 268px; width: 442px; height: 28px; }
  .banner--628 .headline-key { left: 61px; top: 228px; font-size: 70px; }
  .banner--628 .subtitle-panel { left: 67px; top: 331px; width: 342px; height: 99px; }
  .banner--628 .subtitle-text { left: 98px; top: 349px; font-size: 25px; }
  .banner--628 .cta-button { left: 578px; top: 345px; width: 248px; height: 54px; font-size: 21px; }

  /* 1510x196 */
  .banner--strip .brand-name { left: 41px; top: 37px; font-size: 31px; }
  .banner--strip .brand-byline { left: 100px; width: 137px; top: 71px; font-size: 16px; }
  .banner--strip .headline-bar { left: 289px; top: 35px; width: 380px; height: 14px; }
  .banner--strip .headline-line {
    position: absolute; left: 297px; top: 24px; font-size: 24px; line-height: 1; white-space: nowrap;
  }
  .banner--strip .headline-line .lead { font-weight: 300; }
  .banner--strip .headline-line .key { font-weight: 800; }
  .banner--strip .subtitle-panel { left: 309px; top: 61px; width: 341px; height: 65px; }
  .banner--strip .subtitle-text { left: 325px; top: 73px; font-size: 15.5px; line-height: 1.45; }
  .banner--strip .cta-button { left: 851px; top: 75px; width: 185px; height: 39px; font-size: 16px; letter-spacing: 1.5px; }
</style>
</head>
<body>
<main class="sheet">

  <p class="size-label" style="top:160px;">1200x670</p>
  <section class="banner banner--670">
    <div class="stadium-photo" role="img" aria-label="Floodlit football stadium at night with a white quadcopter drone hovering in the foreground"></div>
    <p class="brand-name">SkyMindful</p>
    <p class="brand-byline">By Corvane</p>
    <h1 class="headline-lead">Guide to UAS Risk</h1>
    <div class="headline-bar"></div>
    <p class="headline-key">MITIGATION</p>
    <div class="subtitle-panel">
      <svg viewBox="0 0 342 100" preserveAspectRatio="none"><polygon points="0,5 342,0 328,92 10,100" fill="var(--panel)" stroke="var(--panel-edge)" stroke-width="1"/></svg>
    </div>
    <p class="subtitle-text"><span class="step-count">5 Steps</span> to Develop Your<br>Comprehensive UAS</p>
    <a class="cta-button">GET IT HERE</a>
  </section>

  <p class="size-label" style="top:618px;">1200x628</p>
  <section class="banner banner--628">
    <div class="stadium-photo" role="img" aria-label="Floodlit football stadium at night with a white quadcopter drone hovering in the foreground"></div>
    <p class="brand-name">SkyMindful</p>
    <p class="brand-byline">By Corvane</p>
    <h1 class="headline-lead">Guide to UAS Risk</h1>
    <div class="headline-bar"></div>
    <p class="headline-key">MITIGATION</p>
    <div class="subtitle-panel">
      <svg viewBox="0 0 342 99" preserveAspectRatio="none"><polygon points="0,5 342,0 328,91 10,99" fill="var(--panel)" stroke="var(--panel-edge)" stroke-width="1"/></svg>
    </div>
    <p class="subtitle-text"><span class="step-count">5 Steps</span> to Develop Your<br>Comprehensive UAS</p>
    <a class="cta-button">GET IT HERE</a>
  </section>

  <section class="banner banner--strip">
    <div class="stadium-photo" role="img" aria-label="Wide view of a floodlit stadium crowd with a white quadcopter drone on the right"></div>
    <p class="brand-name">SkyMindful</p>
    <p class="brand-byline">By Corvane</p>
    <div class="headline-bar"></div>
    <h1 class="headline-line"><span class="lead">Guide to UAS Risk </span><span class="key">MITIGATION</span></h1>
    <div class="subtitle-panel">
      <svg viewBox="0 0 341 65" preserveAspectRatio="none"><polygon points="0,4 341,0 321,58 10,65" fill="var(--panel)" stroke="var(--panel-edge)" stroke-width="1"/></svg>
    </div>
    <p class="subtitle-text"><span class="step-count">5 Steps</span> to Develop Your Comprehensive<br>UAS Defense Program</p>
    <a class="cta-button">GET IT HERE</a>
  </section>

</main>
</body>
</html>
```